GUARANTEE PAY GIFT CARD DESIGN

This is a GIFT BONUS CARD

SIZE: 3.5INCH x 2INCH, 8.9cm x 5.1cm, DOUBLE SIDE
Orange must be used as an accent or primary colour.
#F37021, CMYK 0, 54, 86, 5

"BONUS CARD" AND "$20" MUST BE PART OF THE DESIGN.

Please see the attached logo
DO NOT use ribbons or gift box illustrations in the design.

***Terms and conditions must be on the back side of the card-
"No Cash Value. Card valid from 1/2/2024 to 3/31/2024. Valid for Riverside location only. Valid for Dine-in only. Not valid for online togo, delivery, or special events. "

Target Market(s)

40-60 YEARS OLD

Industry/Entity Type

Modern casual malaysian restaurant

Requirements
Must have
• ORANGE COLOUR, BONUS CARD, $20
Should not have
• Ribbons, gift box, CHOPSTICKS, BOWL, NOODLES, CHARATER ILLUSTRATIONS.

```html
<!DOCTYPE html>
<html lang="en">
<head>
<meta charset="utf-8">
<title>Lada Kitchen – $20 Bonus Card</title>
<link rel="stylesheet" href="https://fonts.googleapis.com/css2?family=Antonio:wght@200;300;400&family=Josefin+Sans:wght@300&display=swap">
<style>
  :root {
    --stage: #535353;
    --orange: #f2920f;
    --white: #ffffff;
    --shadow: rgba(0, 0, 0, 0.35);
  }
  * { margin: 0; padding: 0; box-sizing: border-box; }
  html, body { width: 1200px; height: 1175px; overflow: hidden; }
  body { background: var(--stage); position: relative; font-family: "Antonio", sans-serif; }

  .card {
    position: absolute;
    left: 208px;
    width: 783px;
    height: 448px;
    box-shadow: 0 14px 28px var(--shadow);
    overflow: hidden;
  }
  .card-front { top: 101px; background: var(--orange); }
  .card-back { top: 597px; background: var(--white); }
  .card-shapes { position: absolute; inset: 0; }

  /* Front */
  .value {
    position: absolute;
    left: 127px;
    top: 10px;
    font-weight: 300;
    font-size: 228px;
    line-height: 1;
    color: var(--white);
    letter-spacing: 6px;
    transform: scaleX(1.2);
    transform-origin: left top;
  }
  .currency {
    position: absolute;
    left: 351px;
    top: 46px;
    font-weight: 400;
    font-size: 82px;
    line-height: 1;
    color: var(--white);
  }
  .card-title {
    position: absolute;
    left: 125px;
    width: 214px;
    color: var(--white);
    line-height: 1;
  }
  .card-title-bonus {
    top: 236px;
    font-weight: 300;
    font-size: 105px;
    text-align: center;
    letter-spacing: -1px;
    color: transparent;
    -webkit-text-stroke: 1.3px var(--white);
  }
  .card-title-card {
    top: 341px;
    font-weight: 400;
    font-size: 66px;
    display: flex;
    justify-content: space-between;
  }
  .brand-badge {
    position: absolute;
    left: 537px;
    top: 237px;
    width: 174px;
    height: 174px;
    border-radius: 50%;
    background: var(--orange);
    display: flex;
    align-items: center;
    justify-content: center;
  }
  .brand-badge .brand-name {
    font-family: "Josefin Sans", sans-serif;
    font-weight: 300;
    font-size: 29px;
    line-height: 1.05;
    letter-spacing: 2px;
    color: var(--white);
    text-align: center;
    text-transform: uppercase;
  }

  /* Back */
  .back-brand {
    position: absolute;
    left: 384px;
    top: 78px;
    font-family: "Josefin Sans", sans-serif;
    font-weight: 300;
    font-size: 43px;
    letter-spacing: 1px;
    color: var(--orange);
    text-transform: uppercase;
    line-height: 1;
    white-space: nowrap;
  }
  .terms {
    position: absolute;
    left: 48px;
    top: 260px;
    color: var(--white);
    text-transform: uppercase;
  }
  .terms-title {
    font-weight: 300;
    font-size: 16px;
    line-height: 1.2;
    padding-bottom: 1px;
    border-bottom: 1.5px solid var(--white);
    display: inline-block;
    padding-right: 2px;
  }
  .terms-list {
    list-style: none;
    margin-top: 5px;
    padding-left: 7px;
    font-weight: 300;
    font-size: 12.5px;
    line-height: 17.3px;
  }
</style>
</head>
<body>

<section class="card card-front" aria-label="Bonus card front">
  <svg class="card-shapes" width="783" height="448" viewBox="0 0 783 448" aria-hidden="true">
    <defs>
      <pattern id="scallop-left" x="507" y="0" width="14" height="12" patternUnits="userSpaceOnUse">
        <circle cx="7" cy="6" r="6" fill="#ffffff"/>
      </pattern>
      <pattern id="scallop-right" x="720" y="0" width="14" height="12" patternUnits="userSpaceOnUse">
        <circle cx="7" cy="6" r="6" fill="#ffffff"/>
      </pattern>
    </defs>
    <rect x="514" y="0" width="213" height="448" fill="#ffffff"/>
    <rect x="507" y="0" width="14" height="448" fill="url(#scallop-left)"/>
    <rect x="720" y="0" width="14" height="448" fill="url(#scallop-right)"/>
  </svg>

  <div class="value">20</div>
  <div class="currency">$</div>
  <div class="card-title card-title-bonus">BONUS</div>
  <div class="card-title card-title-card"><span>C</span><span>A</span><span>R</span><span>D</span></div>

  <div class="brand-badge">
    <span class="brand-name">Lada<br>Kitchen</span>
  </div>
</section>

<section class="card card-back" aria-label="Bonus card back">
  <svg class="card-shapes" width="783" height="448" viewBox="0 0 783 448" aria-hidden="true">
    <defs>
      <pattern id="scallop-top" x="0" y="200" width="15" height="12" patternUnits="userSpaceOnUse">
        <circle cx="7.5" cy="6" r="6" fill="#f2920f"/>
      </pattern>
      <pattern id="scallop-bottom" x="0" y="406" width="15" height="12" patternUnits="userSpaceOnUse">
        <circle cx="7.5" cy="6" r="6" fill="#f2920f"/>
      </pattern>
    </defs>
    <rect x="0" y="206" width="783" height="206" fill="#f2920f"/>
    <rect x="0" y="200" width="783" height="12" fill="url(#scallop-top)"/>
    <rect x="0" y="406" width="783" height="12" fill="url(#scallop-bottom)"/>
  </svg>

  <div class="back-brand">Lada Kitchen</div>

  <div class="terms">
    <div class="terms-title">*Terms and Conditions</div>
    <ul class="terms-list">
      <li>No cash value</li>
      <li>Card valid from 1/2/2024 to 3/31/2024</li>
      <li>Valid for Riverside location only</li>
      <li>Valid for dine-in only</li>
      <li>Not valid for online togo, delivery, or special events</li>
    </ul>
  </div>
</section>

</body>
</html>
```